Best in class business looking for best in class stationery that accurately reflects the brand image we are trying to build as the brand expands throughout the country. The Varying items should be an eye catching design that makes even the simplest letter or small business card stand out in the crowd.

Target Market(s)

Professionals

Industry/Entity Type

Real Estate

Other font styles liked:
• See atttached logo

Requirements
Must have
• Letterhead
• Business cards
• Envelopes
• Labels for larger mailings
Nice to have
• Folders
• Notebook
Should not have
• Stale design elements

```html
<!DOCTYPE html>
<html lang="en">
<head>
<meta charset="utf-8">
<title>Cedar Crest Management – Business Card</title>
<link rel="stylesheet" href="https://fonts.googleapis.com/css2?family=Source+Sans+3:wght@400;600&display=swap">
<style>
  :root {
    --stage: #b4b4b4;
    --card-white: #f7f7f7;
    --navy: #24317a;
    --navy-deep: #232e74;
    --band-light: #3b64b9;
    --ink: #3a3a3a;
    --white: #ffffff;
  }
  * { margin: 0; padding: 0; box-sizing: border-box; }
  html, body {
    width: 1200px; height: 750px; overflow: hidden;
    background: var(--stage);
    font-family: "Source Sans 3", sans-serif;
  }
  .stage { position: relative; width: 1200px; height: 750px; }
  .card {
    position: absolute; top: 228px; width: 461px; height: 263px;
  }
  .card--front { left: 138px; background: var(--card-white); }
  .card--back { left: 607px; background: var(--navy-deep); }

  .name-band {
    position: absolute; left: 0; top: 26px; width: 100%; height: 51px;
    background: linear-gradient(90deg, var(--navy) 0%, var(--navy) 55%, var(--band-light) 100%);
    color: var(--white); padding: 8px 0 0 24px;
  }
  .person-name { font-size: 17px; font-weight: 600; line-height: 1.15; letter-spacing: 0.2px; }
  .person-title { font-size: 13px; font-weight: 400; line-height: 1.3; }

  .brand {
    position: absolute; right: 26px; top: 86px;
    display: flex; align-items: center; gap: 7px;
    color: var(--navy); font-size: 13px; font-weight: 600;
    text-transform: uppercase; letter-spacing: 0.4px;
  }
  .brand-square { width: 10px; height: 10px; background: var(--navy); }

  .contact-list {
    position: absolute; left: 25px; top: 176px; list-style: none;
    font-size: 12.5px; color: var(--ink); line-height: 17.6px;
  }
  .contact-list li { display: flex; align-items: center; gap: 6px; }
  .contact-list svg { width: 11px; height: 11px; fill: var(--navy); flex: none; }

  .address {
    position: absolute; right: 26px; top: 193px; text-align: right;
    font-size: 12.5px; color: var(--ink); line-height: 17.6px; font-style: normal;
  }

  .back-brand {
    position: absolute; right: 34px; top: 34px; text-align: center; color: var(--white);
  }
  .back-brand-name {
    font-size: 13px; font-weight: 600; text-transform: uppercase; letter-spacing: 0.4px;
  }
  .back-url { margin-top: 10px; font-size: 12px; letter-spacing: 1.1px; }
</style>
</head>
<body>
<main class="stage">
  <section class="card card--front" aria-label="Business card front">
    <div class="name-band">
      <p class="person-name">DANIEL REYES</p>
      <p class="person-title">CEO/Founder</p>
    </div>
    <div class="brand"><span class="brand-square"></span>Cedar Crest Management Corporation</div>

    <ul class="contact-list">
      <li><svg viewBox="0 0 12 12"><path d="M2.5 0.5 L4.5 0.5 L5 3.2 L3.6 4.3 C4.3 5.9 5.8 7.5 7.7 8.4 L8.8 7 L11.5 7.5 L11.5 9.6 C11.5 10.8 10.6 11.5 9.6 11.4 C5 11 1 7 0.6 2.4 C0.5 1.4 1.2 0.5 2.5 0.5 Z"/></svg>555 214 7730</li>
      <li><svg viewBox="0 0 12 12"><path d="M3 0 H9 A1 1 0 0 1 10 1 V11 A1 1 0 0 1 9 12 H3 A1 1 0 0 1 2 11 V1 A1 1 0 0 1 3 0 Z M3.4 1.5 V9.5 H8.6 V1.5 Z"/></svg>555 318 4426</li>
      <li><svg viewBox="0 0 12 12"><path d="M3 0 H8 L9 1 V4 H3 Z M0.5 5 H11.5 V9 H9.5 V7.5 H2.5 V9 H0.5 Z M3 8.3 H9 V12 H3 Z"/></svg>555 902 6158</li>
      <li><svg viewBox="0 0 12 12"><path d="M0.5 2 H11.5 V10 H0.5 Z M1.3 2.8 L6 6.6 L10.7 2.8 Z"/></svg>daniel@cedarcrestmgmt.com</li>
    </ul>

    <address class="address">
      4120 Larkspur Court<br>
      Boise, Idaho 83702<br>
      www.cedarcrestmgmt.com
    </address>
  </section>

  <section class="card card--back" aria-label="Business card back">
    <div class="back-brand">
      <p class="back-brand-name">Cedar Crest Management Corporation</p>
      <p class="back-url">www.cedarcrestmgmt.com</p>
    </div>
  </section>
</main>
</body>
</html>
```